German Headhunter/ HR Consultancy needs Business Cards Design

We need a business Card Design for our Company in Stuttgart. We are specialized as Headhunter/ HR Consultancy in Placement of specialist and managers in permanent employment. Please refer to our business logo.

```html
<!DOCTYPE html>
<html lang="de">
<head>
<meta charset="utf-8">
<title>Kernwerk Personalberatung – Visitenkarte</title>
<link rel="stylesheet" href="https://fonts.googleapis.com/css2?family=Lato:wght@400;700&family=Oswald:wght@600&display=swap">
<style>
  :root {
    --backdrop: #1d1d1f;
    --card: #111112;
    --accent: #3b55b0;
    --text: #f2f2f2;
    --muted: #8e8e92;
  }
  * { margin: 0; padding: 0; box-sizing: border-box; }
  html, body {
    width: 1200px; height: 900px; overflow: hidden;
    background: var(--backdrop);
  }
  .canvas {
    position: relative; width: 1200px; height: 900px;
  }
  .card {
    position: absolute; left: 280px; width: 640px; height: 366px;
    background: var(--card);
    box-shadow: 0 10px 30px rgba(0,0,0,.55);
    overflow: hidden;
  }
  .card--front { top: 52px; }
  .card--back { top: 482px; }
  .card__band {
    position: absolute; left: 0; right: 0; bottom: 0; height: 11px;
    background: var(--accent);
  }
  .brand {
    position: absolute; top: 0; left: 0; right: 0; bottom: 11px;
    display: flex; align-items: center; justify-content: center; gap: 18px;
  }
  .brand__mark {
    width: 34px; height: 34px; background: var(--accent);
  }
  .brand__name {
    font-family: "Lato", sans-serif; font-weight: 700;
    font-size: 30px; letter-spacing: 2px; text-transform: uppercase;
    color: var(--accent); line-height: 1.15;
  }
  .holder {
    position: absolute; left: 62px; top: 124px; text-align: right; width: 218px;
  }
  .holder__name {
    font-family: "Oswald", sans-serif; font-weight: 600;
    font-size: 34px; line-height: 1.1; text-transform: uppercase;
    color: var(--accent); letter-spacing: .3px;
  }
  .holder__role {
    font-family: "Lato", sans-serif; font-size: 17px; color: var(--text);
    margin-top: 2px;
  }
  .divider {
    position: absolute; left: 304px; top: 132px; width: 1px; height: 94px;
    background: var(--muted);
  }
  .contact {
    position: absolute; left: 326px; top: 142px; list-style: none;
    font-family: "Lato", sans-serif; font-size: 17px; color: var(--text);
  }
  .contact__item {
    display: flex; align-items: center; gap: 10px; height: 27px;
  }
  .contact__icon { width: 16px; height: 16px; flex: none; }
  .address {
    position: absolute; left: 62px; bottom: 44px;
    font-family: "Lato", sans-serif; font-size: 18px; color: var(--text);
  }
</style>
</head>
<body>
<main class="canvas">

  <section class="card card--front" aria-label="Vorderseite">
    <div class="brand">
      <span class="brand__mark" aria-hidden="true"></span>
      <span class="brand__name">Kernwerk<br>Personalberatung</span>
    </div>
    <div class="card__band"></div>
  </section>

  <section class="card card--back" aria-label="Rückseite">
    <div class="holder">
      <h1 class="holder__name">Lukas Brenner</h1>
      <p class="holder__role">Managing Director</p>
    </div>
    <div class="divider"></div>
    <ul class="contact">
      <li class="contact__item">
        <svg class="contact__icon" viewBox="0 0 24 24" fill="#3b55b0" aria-hidden="true"><path d="M6.6 10.8a15.1 15.1 0 0 0 6.6 6.6l2.2-2.2a1 1 0 0 1 1-.25 11.4 11.4 0 0 0 3.6.57 1 1 0 0 1 1 1V20a1 1 0 0 1-1 1A17 17 0 0 1 3 4a1 1 0 0 1 1-1h3.5a1 1 0 0 1 1 1c0 1.25.2 2.45.57 3.57a1 1 0 0 1-.25 1z"/></svg>
        0711-482 905 316
      </li>
      <li class="contact__item">
        <svg class="contact__icon" viewBox="0 0 24 24" fill="#3b55b0" aria-hidden="true"><path d="M2 5h20v14H2z" fill="none" stroke="#3b55b0" stroke-width="2"/><path d="M2 5l10 8 10-8" fill="none" stroke="#3b55b0" stroke-width="2"/></svg>
        info@kernwerk-hr.de
      </li>
      <li class="contact__item">
        <svg class="contact__icon" viewBox="0 0 24 24" fill="none" stroke="#3b55b0" stroke-width="2" aria-hidden="true"><circle cx="12" cy="12" r="10"/><path d="M2 12h20M12 2c3 3 3 17 0 20M12 2c-3 3-3 17 0 20"/></svg>
        www.kernwerk-hr.de
      </li>
    </ul>
    <p class="address">18, Lindenstraße 42, Stuttgart, 70173</p>
    <div class="card__band"></div>
  </section>

</main>
</body>
</html>
```